Verpackungsdesign für Räucherstäbchen
Zielgruppe
Unsere Firma Lindenkram importiert hochwertige und reine Räucherstoffe aus entfernten Ländern. Dabei steht die Nachhaltigkeit und der faire Handel im Vordergrund. Unser Fokus ist dabei der Handel mit Weihrauch, den wir aus den Ursprungsländern importieren und an Großhändler, Händler und Endkunden weiterverkaufen. Seit einigen Jahren haben wir den Wunsch echte, natürliche Räucherstäbchen auf den Markt zu bringen. Dieses Projekt wurde nun umgesetzt.
Wir suchen ein Verpackungsdesign für unsere Räucherstäbchen. Die Räucherstäbchen sind absolut naturrein (95% aller Räucherstäbchen auf dem Markt sind es nicht), ohne Chemie, ohne Parfum, ohne Synthetik. Absolut rein, hergestellt aus besten Rohstoffen, teilweise direkt aus Deutschland.
Aufgabenstellung
Da die Räucherstäbchen auch in den Handel kommen werden, ist es am Besten, dass die Verpackung eine Faltschachtel ist mit den Maßen: 6cm Breite, 22cm Länge, 1,5cm Höhe
Die Schachtel sollte sehr natürlich ausschauen und die Farben nicht zu kräftig.
Es wird ein Logo darauf geben, das ich hochladen werde.
Farben sollten natürlich sein, Elegant und natürlich. Wir wissen nicht genau, wie die Verpackung aussehen soll, doch sicher ist, dass sie nicht zu überladen sein sollte. Die Verpackung sollte schlicht, natürlich und edel sein
Wir planen über 20 Sorten: Harze, Sandelholz, Patchouli etc.
Das Design der Verpackung sollte das berücksichtigen. Ein Design, das später an die verschiedenen Sorten angepasst werden kann
Für das Beispiel-Design:
Text auf der Vorderseite:
Räucherstäbchen
Weihrauch Afrika
Made with love in Germany
Natur pur
Rückseite:
Naturreine Räucherstäbchen hergestellt mit den reinsten Rohstoffen
Ohne chemische oder synthetische Zusätze, kein Parfum, keine Abbrennhilfe
Brenndauer: ca. 45- 60min
Eine Verpackung beinhaltet 10 Räucherstäbchen.
Hergestellt von:
Made by
Lindenkram
Birkenauer Weg 14
68519 Ahornfeld

```html
<!DOCTYPE html>
<html lang="de">
<head>
<meta charset="utf-8">
<title>Räucherstäbchen – Faltschachtel Weihrauch Afrika</title>
<link href="https://fonts.googleapis.com/css2?family=Alegreya:wght@400;500&family=Open+Sans:wght@400;600&display=swap" rel="stylesheet">
<style>
  :root{
    --bg:#f3f1ee;
    --maroon:#5a1a17;
    --maroon-line:#7a2a26;
    --cream:#fcf0dc;
    --label-ink:#6b2420;
    --gold:#f2c77e;
    --leaf-a:#f0c37a;
    --leaf-b:#d9773f;
    --leaf-c:#7a2f22;
    --green:#6f8a4a;
  }
  html,body{margin:0;padding:0;width:1200px;height:848px;overflow:hidden;background:var(--bg);}
  .canvas{position:relative;width:1200px;height:848px;}
  .dieline{position:absolute;left:600px;top:424px;width:424px;height:708px;transform:translate(-50%,-50%) scale(1.12);transform-origin:center;}
  .part{position:absolute;background:var(--maroon);box-sizing:border-box;}
  .panel-outline{border:1px solid var(--maroon-line);}
  .tuck{position:absolute;background:var(--cream);}
  .pattern{position:absolute;top:43px;height:390px;width:170px;
    background:radial-gradient(ellipse at 40% 60%,var(--leaf-a) 0%,var(--leaf-b) 35%,var(--leaf-c) 75%,var(--maroon) 100%);}
  .label{position:absolute;top:43px;width:134px;height:215px;background:var(--cream);
    display:flex;flex-direction:column;align-items:center;font-family:"Alegreya",serif;color:var(--label-ink);text-align:center;}
  .label-title{margin-top:62px;font-size:19px;line-height:26px;letter-spacing:.5px;font-weight:500;}
  .label-dot{margin:26px 0 22px;width:6px;height:6px;border:1px solid var(--label-ink);border-radius:50%;}
  .label-variant{font-size:14px;line-height:20px;letter-spacing:.3px;}
  .back-copy{position:absolute;left:20px;top:448px;width:126px;font-family:"Open Sans",sans-serif;font-size:7.2px;line-height:10px;color:var(--gold);}
  .back-copy p{margin:0 0 10px;}
  .back-copy strong{font-weight:600;}
  .front-claim{position:absolute;left:212px;width:170px;text-align:center;color:var(--gold);}
  .claim-natur{top:450px;font-family:"Alegreya",serif;font-size:14px;}
  .claim-love{top:500px;font-family:"Open Sans",sans-serif;font-size:9.5px;font-weight:600;}
  .brand{position:absolute;left:212px;top:560px;width:170px;display:flex;flex-direction:column;align-items:center;}
  .brand-circle{width:54px;height:54px;border:1px solid var(--green);border-radius:50%;}
  .brand-name{margin-top:6px;font-family:"Open Sans",sans-serif;font-weight:600;font-size:10px;color:var(--green);}
</style>
</head>
<body>
<div class="canvas">
  <div class="dieline">
    <!-- back panel -->
    <div class="tuck" style="left:18px;top:0;width:134px;height:43px;"></div>
    <div class="part panel-outline" style="left:0;top:43px;width:170px;height:622px;"></div>
    <div class="pattern" style="left:0;" role="img" aria-label="Ornamentales Blattmuster in Gold, Orange und Rotbraun"></div>
    <div class="label" style="left:18px;">
      <div class="label-title">RÄUCHER<br>STÄBCHEN</div>
      <div class="label-dot"></div>
      <div class="label-variant">WEIHRAUCH<br>AFRIKA</div>
    </div>
    <div class="back-copy">
      <p>Naturreine Räucherstäbchen hergestellt mit den reinsten Rohstoffen. Ohne chemische oder synthetische Zusätze, kein Parfum, keine Abbrennhilfe.</p>
      <p><strong>Brenndauer:</strong>&nbsp; ca. 45- 60min</p>
      <p>Eine Verpackung beinhaltet<br><strong>10 Räucherstäbchen.</strong></p>
      <p><strong>Hergestellt von:</strong></p>
      <p>Made by<br>Lindenkram<br>Birkenauer Weg 14<br>68519 Ahornfeld</p>
    </div>

    <!-- side panel -->
    <div class="part panel-outline" style="left:170px;top:43px;width:42px;height:622px;"></div>

    <!-- front panel -->
    <div class="part panel-outline" style="left:212px;top:0;width:170px;height:665px;"></div>
    <div class="tuck" style="left:230px;top:0;width:134px;height:43px;"></div>
    <div class="pattern" style="left:212px;" role="img" aria-label="Ornamentales Blattmuster in Gold, Orange und Rotbraun"></div>
    <div class="label" style="left:230px;">
      <div class="label-title">RÄUCHER<br>STÄBCHEN</div>
      <div class="label-dot"></div>
      <div class="label-variant">WEIHRAUCH<br>AFRIKA</div>
    </div>
    <div class="front-claim claim-natur">NATUR PUR</div>
    <div class="front-claim claim-love">Made with love in Germany</div>
    <div class="brand">
      <div class="brand-circle"></div>
      <div class="brand-name">lindenkram.de</div>
    </div>

    <!-- glue flap and bottom flap -->
    <div class="part panel-outline" style="left:382px;top:43px;width:42px;height:622px;"></div>
    <div class="part panel-outline" style="left:212px;top:665px;width:170px;height:43px;"></div>
  </div>
</div>
</body>
</html>
```